Business card design needed

We are a gardening company who handle:
All Forms of gardens work including
Mowing
Pruning
edging
weeding
Poisoning
Landscaping
Minor Stump Removal
Rubbish Removal
and more

I want a card that look professional not cartoon style

Harlow Yards and Lawncare Service

Dean Marsholt
0486259041

```html
<!DOCTYPE html>
<html lang="en">
<head>
<meta charset="utf-8">
<title>Harlow Yards and Lawncare Service – Business Card</title>
<link rel="stylesheet" href="https://fonts.googleapis.com/css2?family=Source+Sans+3:wght@400;600&display=swap">
<style>
  :root {
    --page-bg: #2e2e30;
    --card-face-top: #727274;
    --card-face-bottom: #58585a;
    --side-band: #474749;
    --tile-light: #d9d9d9;
    --tile-dark: #626264;
    --ink-bright: #ffffff;
    --ink-soft: #e6e6e6;
    --ink-muted: #cfcfcf;
  }
  * { margin: 0; padding: 0; box-sizing: border-box; }
  html, body {
    width: 1200px;
    height: 871px;
    overflow: hidden;
    background: var(--page-bg);
    font-family: "Source Sans 3", "Myriad Pro", Arial, sans-serif;
  }
  .canvas {
    position: relative;
    width: 1200px;
    height: 871px;
  }
  .business-card {
    position: absolute;
    left: 120px;
    top: 162px;
    width: 960px;
    height: 548px;
    background: linear-gradient(160deg, var(--card-face-top) 0%, var(--card-face-bottom) 100%);
    box-shadow: 0 18px 40px rgba(0,0,0,0.45);
    overflow: hidden;
  }
  .side-band {
    position: absolute;
    left: 0;
    top: 0;
    width: 150px;
    height: 100%;
    background: var(--side-band);
  }
  .tile-column {
    position: absolute;
    left: 150px;
    top: 0;
    width: 44px;
    height: 100%;
    display: flex;
    flex-direction: column;
  }
  .tile-column span { flex: 1; }
  .tile-column span:nth-child(1) { background: #dcdcdc; }
  .tile-column span:nth-child(2) { background: #c2c2c2; }
  .tile-column span:nth-child(3) { background: #a9a9aa; }
  .tile-column span:nth-child(4) { background: #939394; }
  .tile-column span:nth-child(5) { background: #808081; }
  .tile-column span:nth-child(6) { background: #717172; }
  .tile-column span:nth-child(7) { background: #676769; }
  .tile-column span:nth-child(8) { background: #5f5f61; }
  .brand-block {
    position: absolute;
    right: 62px;
    top: 66px;
    text-align: right;
    color: var(--ink-bright);
  }
  .brand-name {
    font-size: 60px;
    font-weight: 400;
    line-height: 1;
    letter-spacing: 0.5px;
  }
  .brand-tagline {
    font-size: 44px;
    font-weight: 400;
    line-height: 1.1;
    color: var(--ink-soft);
    letter-spacing: 0.5px;
  }
  .person-block {
    position: absolute;
    right: 62px;
    top: 268px;
    text-align: right;
  }
  .person-name {
    font-size: 34px;
    color: var(--ink-soft);
    line-height: 1.1;
  }
  .person-role {
    font-size: 14px;
    color: var(--ink-muted);
    letter-spacing: 1px;
  }
  .divider {
    position: absolute;
    left: 430px;
    right: 62px;
    top: 360px;
    height: 3px;
    background: linear-gradient(90deg, rgba(255,255,255,0.95), rgba(255,255,255,0.55));
  }
  .contact-block {
    position: absolute;
    right: 62px;
    top: 372px;
    text-align: right;
    color: var(--ink-soft);
    font-size: 21px;
    line-height: 1.3;
    letter-spacing: 0.6px;
  }
  .contact-block .phone { font-size: 22px; }
</style>
</head>
<body>
<main class="canvas">
  <section class="business-card" aria-label="Business card">
    <div class="side-band"></div>
    <div class="tile-column" aria-hidden="true">
      <span></span><span></span><span></span><span></span>
      <span></span><span></span><span></span><span></span>
    </div>

    <header class="brand-block">
      <h1 class="brand-name">Harlow Yards</h1>
      <p class="brand-tagline">Lawncare Service</p>
    </header>

    <div class="person-block">
      <p class="person-name">Dean Marsholt</p>
      <p class="person-role">CEO</p>
    </div>

    <div class="divider"></div>

    <address class="contact-block" style="font-style: normal;">
      <p>14 WILLOW BEND ROAD WESTFIELD</p>
      <p>ASHFORD / ENGLAND</p>
      <p class="phone">0486 259 041</p>
      <p class="phone">0471 830 562</p>
    </address>
  </section>
</main>
</body>
</html>
```